New Label Design Project

We need to create a label for a new product that you spray onto your car to wax the vehicle after a wash. We have a very limited amount of time to create this label. How the Product Works: Spray onto your vehicle surface when its still wet, right after the rinse step of a Car Wash. You spray it on, and the Wax adheres on-contact in seconds. After you've sprayed the product on your car you rinse your vehicle and BAM your car is waxed.

```html
<!DOCTYPE html>
<html lang="en">
<head>
<meta charset="UTF-8">
<title>Wax Spray – High Gloss Label</title>
<link rel="stylesheet" href="https://fonts.googleapis.com/css2?family=Orbitron:wght@900&family=Exo+2:wght@300&display=swap">
<style>
  :root {
    --ink-black: #000000;
    --flag-dark: #1b2530;
    --flag-mid: #2e3034;
    --race-red: #e3202a;
    --paint-red: #e8262c;
    --paint-deep: #8e0f12;
    --gloss-white: #ffffff;
  }
  html, body {
    margin: 0;
    padding: 0;
    width: 1010px;
    height: 1200px;
    overflow: hidden;
    background: var(--ink-black);
  }
  .label {
    position: relative;
    width: 1010px;
    height: 1200px;
    overflow: hidden;
  }
  .label-art {
    position: absolute;
    inset: 0;
    display: block;
  }
  .product-title {
    font-family: "Orbitron", sans-serif;
    font-weight: 900;
    fill: var(--race-red);
  }
  .product-tagline {
    font-family: "Exo 2", sans-serif;
    font-weight: 300;
    fill: var(--gloss-white);
  }
</style>
</head>
<body>
<main class="label">
  <svg class="label-art" width="1010" height="1200" viewBox="0 0 1010 1200" xmlns="http://www.w3.org/2000/svg">
    <defs>
      <linearGradient id="flag-tone" x1="0" y1="0" x2="1" y2="1">
        <stop offset="0" stop-color="var(--flag-mid)"/>
        <stop offset="1" stop-color="var(--flag-dark)"/>
      </linearGradient>
      <linearGradient id="paint-tone" x1="0" y1="0" x2="1" y2="1">
        <stop offset="0" stop-color="var(--paint-red)"/>
        <stop offset="0.6" stop-color="#c8161c"/>
        <stop offset="1" stop-color="var(--paint-deep)"/>
      </linearGradient>
    </defs>

    <rect class="flag-backdrop" role="img" aria-label="Waving black and grey chequered racing flag"
          x="0" y="0" width="1010" height="1200" fill="url(#flag-tone)"/>

    <path class="title-wave" fill="var(--ink-black)"
          d="M0,585 C150,565 225,430 330,305 C430,200 560,190 700,232 C820,262 905,178 1010,112 L1010,1200 L0,1200 Z"/>

    <path class="car-photo" role="img" aria-label="Close-up photo of a glossy red sports car with a polished alloy wheel"
          fill="url(#paint-tone)"
          d="M0,1000 C150,900 330,650 520,520 C640,440 760,560 820,570 C880,580 950,520 1010,585 L1010,1200 L0,1200 Z"/>

    <path class="flag-corner" role="img" aria-label="Corner of chequered racing flag"
          fill="url(#flag-tone)"
          d="M440,1200 C560,1080 700,928 822,928 C900,928 960,948 1010,962 L1010,1200 Z"/>

    <text class="product-title" x="323" y="230" textLength="363" lengthAdjust="spacingAndGlyphs" font-size="100">WAX</text>
    <text class="product-title" x="242" y="364" textLength="533" lengthAdjust="spacingAndGlyphs" font-size="100">SPRAY</text>
    <text class="product-tagline" x="327" y="468" textLength="355" lengthAdjust="spacingAndGlyphs" font-size="60">high gloss</text>
  </svg>
</main>
</body>
</html>
```